White Dove Release Postcard for Event Planners

We require a double-sided Postcard (8.5" x 5.5") that will be mailed to Event Planners advising them of our White Dove Release services for weddings, anniversaries, and other happy events.

Wingsong Moments is the originator of White Dove Releases in the greater Toronto area, adding a beautiful moment to weddings and other celebrations since 1995.

A professional release of Pure White Doves is a natural part of wedding ceremonies, lending a special celebratory note to the exchange of vows. White Doves are the living symbol of everlasting love, fidelity, peace and harmony. These lovely birds mate for life, building a home and raising their young together.

For more information, please visit www.wingsongmoments.example

Target Market(s)

Event and Wedding Planners. Primarily for weddings but could be for other types of celebratory events.

Industry/Entity Type

Events

Requirements
Must have
• Space for address label and stamp to be affixed.
• Pictures of beautiful brides with doves (see attachments).
Nice to have
• Multicultural weddings / brides
Should not have
• No religious images. Must be non-denominational.

```html
<!DOCTYPE html>
<html lang="en">
<head>
<meta charset="utf-8">
<title>Wingsong Moments Postcard</title>
<link rel="stylesheet" href="https://fonts.googleapis.com/css2?family=Cinzel:wght@400;700&family=Montserrat:ital,wght@0,400;0,600;0,700;1,700&display=swap">
<style>
  :root {
    --stage: #3b3b3b;
    --purple: #5b3a8c;
    --purple-deep: #4a2c78;
    --lavender: #e7e1ef;
    --lavender-mid: #b9a6d3;
    --ink: #1e1a24;
    --lime: #b5e04a;
    --white: #ffffff;
    --rule: #8d8796;
  }
  * { margin: 0; padding: 0; box-sizing: border-box; }
  html, body { width: 1200px; height: 646px; overflow: hidden; background: var(--stage); }
  body { position: relative; font-family: "Montserrat", sans-serif; color: var(--ink); }

  .card { position: absolute; top: 57px; width: 570px; height: 370px; overflow: hidden; }
  .card--front { left: 20px; background: var(--lavender); }
  .card--back { left: 610px; background: var(--white); }

  .abs { position: absolute; }

  /* front */
  .front-header-art { left: 0; top: 0; width: 570px; height: 138px;
    background: linear-gradient(100deg, #8d72b8 0%, #b7a2d6 45%, #9c82c4 75%, #7e63ad 100%); }
  .front-photo { left: 250px; top: 138px; width: 320px; height: 232px;
    background: linear-gradient(180deg, #3f5a2c 0%, #6f8a4e 40%, #cfd4c8 70%, #e8e8ea 100%); }
  .front-band { left: 0; top: 138px; width: 570px; height: 70px;
    background: linear-gradient(90deg, var(--purple) 0%, var(--purple) 55%, rgba(91,58,140,0.55) 100%); }
  .front-fade { left: 0; top: 208px; width: 360px; height: 162px;
    background: linear-gradient(90deg, var(--lavender) 65%, rgba(231,225,239,0) 100%); }

  .kicker { font-family: "Cinzel", serif; font-weight: 400; text-align: center; }
  .brand { font-family: "Cinzel", serif; font-weight: 700; text-align: center; white-space: nowrap; }
  .services { font-family: "Cinzel", serif; font-weight: 700; text-align: center; white-space: nowrap; }
  .since { font-family: "Cinzel", serif; text-align: center; }

  .front .kicker { left: 0; width: 570px; top: 14px; font-size: 19px; color: var(--ink); }
  .front .brand { left: 0; width: 570px; top: 36px; font-size: 41px; color: var(--ink); letter-spacing: 0.5px; }
  .front .services { left: 0; width: 570px; top: 88px; font-size: 15px; color: var(--white); }
  .front .since { left: 0; width: 570px; top: 113px; font-size: 13.5px; color: var(--ink); }

  .band-title { left: 18px; top: 152px; font-size: 13px; font-weight: 700; color: var(--white); line-height: 17px; }
  .band-tag { left: 18px; top: 187px; font-size: 9px; font-style: italic; font-weight: 700; color: var(--lime); }

  .benefits { list-style: none; font-size: 8px; line-height: 13.7px; }
  .benefits li::before { content: "\2022"; margin-right: 7px; }
  .front .benefits { left: 18px; top: 224px; color: var(--ink); }

  .contact-lead { font-size: 8.5px; }
  .contact-phone { font-size: 15px; font-weight: 600; line-height: 18px; }
  .contact-web { font-size: 9px; }
  .front .contact { left: 18px; top: 314px; color: var(--purple-deep); }
  .front .contact-web { color: var(--ink); }

  /* back */
  .back-panel { left: 0; top: 0; width: 296px; height: 370px; background: var(--lavender); }
  .back-wave { left: 0; top: 0; }
  .back-dove { left: 26px; top: 228px; width: 90px; height: 130px; border-radius: 45% 45% 40% 40%;
    background: radial-gradient(ellipse at center, #ffffff 0%, #efeaf5 60%, rgba(239,234,245,0) 100%); }
  .back .kicker { left: 0; width: 296px; top: 20px; font-size: 10.5px; }
  .back .brand { left: 0; width: 296px; top: 31px; font-size: 20px; }
  .back .services { left: 0; width: 296px; top: 55px; font-size: 8px; }
  .back .since { left: 0; width: 296px; top: 68px; font-size: 7.5px; }
  .back-title { left: 0; width: 296px; top: 93px; text-align: center; font-size: 10px; color: var(--purple-deep); line-height: 12px; }
  .back-tag { left: 0; width: 296px; top: 116px; text-align: center; font-size: 7.5px; font-style: italic; font-weight: 700; color: var(--purple-deep); }
  .back-rule { left: 22px; top: 132px; width: 252px; height: 1px; background: var(--lavender-mid); }
  .back .benefits { left: 22px; top: 153px; font-size: 7.5px; line-height: 11.5px; }
  .care-note { left: 122px; top: 252px; width: 166px; text-align: center; font-size: 7.5px; line-height: 10.5px; color: var(--purple-deep); }
  .back .contact { left: 115px; top: 323px; color: var(--white); }
  .back .contact-lead { font-size: 7.5px; }
  .back .contact-phone { font-size: 14px; line-height: 16px; }
  .back .contact-web { font-size: 8px; color: var(--white); }

  .stamp-area { left: 390px; top: 13px; width: 150px; height: 94px; background: #f3f2f4; }
  .stamp { left: 478px; top: 23px; width: 56px; height: 72px;
    background: linear-gradient(160deg, #7a5aa8, #5b3a8c); border: 3px solid #fff; outline: 1px dashed #bbb; }
  .postmark { left: 390px; top: 13px; }
  .address-line { left: 313px; width: 216px; height: 1px; background: var(--rule); }
</style>
</head>
<body>

<section class="card card--front front">
  <div class="abs front-header-art" role="img" aria-label="Lilac flowers with white doves in flight"></div>
  <div class="abs front-photo" role="img" aria-label="Bride and groom holding white doves beside a white dove cage at an outdoor ceremony"></div>
  <div class="abs front-band"></div>
  <div class="abs front-fade"></div>

  <p class="abs kicker">Silver Feather Group</p>
  <h1 class="abs brand">WINGSONG MOMENTS</h1>
  <p class="abs services">Weddings • Life Celebrations • Private &amp; Public Events</p>
  <p class="abs since">Serving Southern Ontario Since 1995</p>

  <p class="abs band-title">White Doves for Weddings and Other Celebrations<br>The memory of a White Dove Event lasts forever</p>
  <p class="abs band-tag">Adding a special moment to special events for more than 15 years</p>

  <ul class="abs benefits">
    <li>A natural part of wedding ceremonies… white doves mate for life</li>
    <li>Symbolizes everlasting love, fidelity, peace and harmony</li>
    <li>Animal-friendly and environmentally conscientious</li>
    <li>In keeping with today's values and concerns</li>
    <li>Non-denominational; multi-cultural appeal</li>
    <li>Professional staff, always on time</li>
  </ul>

  <div class="abs contact">
    <p class="contact-lead">For more information, contact Dana</p>
    <p class="contact-phone">Call 416-555-0142</p>
    <p class="contact-web">www.wingsongmoments.example</p>
  </div>
</section>

<section class="card card--back back">
  <div class="abs back-panel"></div>
  <svg class="abs back-wave" width="296" height="370" viewBox="0 0 296 370" aria-hidden="true">
    <path d="M0 262 C60 240 120 290 190 300 C240 306 270 296 296 290 L296 370 L0 370 Z" fill="var(--lavender-mid)"/>
    <path d="M0 270 C60 250 120 300 190 310 C240 316 270 306 296 300 L296 370 L0 370 Z" fill="var(--purple)"/>
  </svg>
  <div class="abs back-dove" role="img" aria-label="White dove in flight"></div>

  <p class="abs kicker">Silver Feather Group</p>
  <h2 class="abs brand">WINGSONG MOMENTS</h2>
  <p class="abs services">Weddings • Life Celebrations • Private &amp; Public Events</p>
  <p class="abs since">Serving Southern Ontario Since 1995</p>

  <p class="abs back-title">White Doves for Weddings and Other Celebrations<br>The memory of a White Dove Event lasts forever</p>
  <p class="abs back-tag">Adding a special moment to special events for more than 15 years</p>
  <div class="abs back-rule"></div>

  <ul class="abs benefits">
    <li>A natural part of wedding ceremonies… white doves mate for life</li>
    <li>Symbolizes everlasting love, fidelity, peace and harmony</li>
    <li>Animal-friendly and environmentally conscientious</li>
    <li>In keeping with today's values and concerns</li>
    <li>Non-denominational; multi-cultural appeal</li>
    <li>Professional staff, always on time</li>
    <li>Easy coordination with photographers/videographers</li>
  </ul>

  <p class="abs care-note">Our White Doves receive the best of care and are fully trained to return to their dovecote upon their release from distances of more than 150 kilometres away.</p>

  <div class="abs contact">
    <p class="contact-lead">For more information, contact Dana</p>
    <p class="contact-phone">Call 416-555-0142</p>
    <p class="contact-web">Visit www.wingsongmoments.example</p>
  </div>

  <div class="abs stamp-area"></div>
  <div class="abs stamp" role="img" aria-label="Postage stamp"></div>
  <svg class="abs postmark" width="150" height="94" viewBox="0 0 150 94" aria-hidden="true" fill="none" stroke="#9a8fb0" stroke-width="1.2">
    <path d="M8 22 q12 -5 24 0 t24 0 t24 0 t24 0 t24 0"/>
    <path d="M8 38 q12 -5 24 0 t24 0 t24 0 t24 0 t24 0"/>
    <path d="M8 54 q12 -5 24 0 t24 0 t24 0 t24 0 t24 0"/>
    <path d="M8 70 q12 -5 24 0 t24 0 t24 0 t24 0 t24 0"/>
  </svg>

  <div class="abs address-line" style="top:201px"></div>
  <div class="abs address-line" style="top:227px"></div>
  <div class="abs address-line" style="top:253px"></div>
  <div class="abs address-line" style="top:278px"></div>
  <div class="abs address-line" style="top:303px"></div>
</section>

</body>
</html>
```